Magazine Cover & Back, Course Overview

Please read this whole description and follow directions before proceeding. Please do not submit multiple designs that look similar. If you submit multiple designs that look similar you will be disqualified and receive a poor rating. A magazine design includes a cover and back. This is a single design and should be submitted as such. Do not submit one design for the front only, then a separate design for the back, then a third mock up. Submit all as a single design. I need a magazine cover and back. The size will be standard paper size, 8-1/2" x 11". It will be used for a course overview, a summary of a boating instruction course. I have attached examples and pictures that can be used. I have also attached required content. The final designs must NOT be AI files. Text must be editable with Adobe Acrobat DC.

Target Market(s)

Military & Government

Industry/Entity Type

Military & Government

Requirements
Must have
• See attached.
Nice to have
• See attached.
Should not have
• See attached.

```html
<!DOCTYPE html>
<html lang="en">
<head>
<meta charset="utf-8">
<title>Diver Support Vessel Training – Course Overview</title>
<link href="https://fonts.googleapis.com/css2?family=Jost:wght@300;400;600;700;800&display=swap" rel="stylesheet">
<style>
  :root {
    --orange: #e95424;
    --white: #ffffff;
    --sky: #2a86e6;
    --sea: #1f4f8a;
    --ink: #3a3a3a;
    --page-bg: #ffffff;
  }
  * { box-sizing: border-box; margin: 0; padding: 0; }
  html, body {
    width: 851px; height: 1200px; overflow: hidden;
    background: var(--page-bg);
    font-family: "Jost", Arial, sans-serif;
  }
  .spread {
    position: absolute; left: 20px; top: 338px;
    width: 811px; height: 524px;
    display: flex;
    border: 1px solid #333;
  }
  .page { position: relative; width: 50%; height: 100%; overflow: hidden; }
  .frame {
    position: absolute; inset: 18px;
    border: 1px solid var(--white);
    pointer-events: none; z-index: 3;
  }

  /* back cover */
  .back { background: var(--orange); color: var(--white); }
  .back .cockpit-photo {
    position: absolute; left: 92px; top: 85px; width: 221px; height: 137px;
    background: var(--white); padding: 4px;
  }
  .back .cockpit-photo div {
    width: 100%; height: 100%;
    background: linear-gradient(180deg, #9aa3ab 0%, #6c7178 45%, #3d4248 100%);
  }
  .highlights {
    position: absolute; left: 0; right: 0; top: 250px;
    text-align: center; font-size: 9px; line-height: 13px;
  }
  .highlight { margin-bottom: 13px; font-weight: 400; }
  .highlight strong { display: block; font-weight: 700; font-size: 9.5px; }

  /* front cover */
  .front { background: var(--white); }
  .front .frame { border-color: var(--orange); }
  .vessel-photo {
    position: absolute; left: 0; right: 0; top: 181px; height: 272px;
    background: linear-gradient(180deg, var(--sky) 0%, #5ea3ec 38%, #6f6a58 44%, var(--sea) 52%, #173d6e 100%);
  }
  .title-block {
    position: absolute; left: 36px; top: 0; width: 199px; height: 209px;
    background: var(--orange); color: var(--white);
    z-index: 2; padding: 107px 0 0 3px;
  }
  .title-block h1 { font-weight: 700; line-height: 1; }
  .title-block .t1 { display: block; font-size: 32px; letter-spacing: 0.5px; }
  .title-block .t2 { display: block; font-size: 21px; letter-spacing: 0.2px; }
  .title-block .t3 { display: block; font-size: 22px; font-weight: 300; letter-spacing: 2.5px; }
  .brand-row {
    position: absolute; left: 0; right: 0; top: 453px; height: 71px;
  }
  .brand-name {
    position: absolute; left: 60px; top: 10px; width: 200px;
    text-align: center; color: var(--ink);
    font-size: 11px; font-weight: 400; letter-spacing: 0.6px; line-height: 1.3;
  }
  .partner-badge { position: absolute; left: 286px; top: 4px; }
</style>
</head>
<body>
  <main class="spread">
    <section class="page back">
      <div class="frame"></div>
      <figure class="cockpit-photo">
        <div role="img" aria-label="Photo of a vessel's wheelhouse with steering wheel, control panel and crew at the helm"></div>
      </figure>
      <div class="highlights">
        <p class="highlight"><strong>To assist Navy Sailors with</strong>Becoming More Proficient Coxswains</p>
        <p class="highlight"><strong>Focused on</strong>Safety &amp; Close-Quarters Maneuvering</p>
        <p class="highlight"><strong>Custom Made Course for</strong>Specific Users, Scenarios and Vessels<br>Based on OIC Involvement,<br>Client Feedback and After Action Reviews</p>
        <p class="highlight"><strong>Taught by</strong>Reputable USCG Licensed Boat Captains</p>
        <p class="highlight"><strong>Includes Useful Aids</strong></p>
      </div>
    </section>

    <section class="page front">
      <div class="frame"></div>
      <div class="vessel-photo" role="img" aria-label="Photo of a grey diver support vessel under way on blue water, flying a flag, with a wooded shore behind"></div>
      <div class="title-block">
        <h1><span class="t1">DIVER</span><span class="t2">SUPPORT VESSEL</span><span class="t3">TRAINING</span></h1>
      </div>
      <div class="brand-row">
        <p class="brand-name">Harbor Line<br>Marine Services, LLC</p>
        <svg class="partner-badge" width="42" height="42" viewBox="0 0 42 42" aria-hidden="true">
          <circle cx="21" cy="21" r="20" fill="#1b1b1b" stroke="#c9a63a" stroke-width="2"/>
        </svg>
      </div>
    </section>
  </main>
</body>
</html>
```